Copper Heron Motor Services needs a logo design

I'm after a logo design for a new Female owned automotive repair workshop in the Queanbeyan/Canberra Australia Area.
We offer repairs on all passenger cars, 4wds and light trucks emphasising a strong honest work ethic and a genuine interest in the customer and their vehicles needs. With business details on the front of the card and what we offer on the back.
I would like a design with a phoenix in multiple colours maybe hovering over a flaming wheel or a car with wheels flaming with the phoenix hovering up out of the flames
Target Market(s)
All Vehicle users
Industry/Entity Type
Automotive
Contact Information for Business Card
On the front
Copper Heron Motor
Maree Tolland Owner/ Mechanic 0413527806
email maree@copperheronmotor.com.au
Website www.copperheronmotorworks.com.au
On the back
All Cars, 4WDs, Light trucks, makes and models
Log book servicing
General vehicle servicing
Major vehicle servicing
brake and clutch servicing and repairs
Suspension repairs
cooling systems
All major and minor mechanical repairs
minor electrical rewiring and repairs
Colors
Designer to choose colors to be used in the design.
Look and feel

```html
<!DOCTYPE html>
<html lang="en">
<head>
<meta charset="utf-8">
<title>Copper Heron Motor – Business Card</title>
<link href="https://fonts.googleapis.com/css2?family=Work+Sans:wght@400;500;600;700&display=swap" rel="stylesheet">
<style>
  :root {
    --stage: #e8e4dd;
    --ink-dark: #0d0c0c;
    --card-white: #ffffff;
    --accent: #f7931e;
    --text-grey: #4a4a4a;
    --text-light: #f2f2f2;
    --line-soft: #f5b35e;
  }
  * { box-sizing: border-box; margin: 0; padding: 0; }
  html, body {
    width: 1200px; height: 900px; overflow: hidden;
    background: var(--stage);
    font-family: "Work Sans", Arial, sans-serif;
  }
  .card {
    position: absolute;
    width: 640px; height: 366px;
    border-radius: 22px;
    overflow: hidden;
    box-shadow: 0 10px 24px rgba(0,0,0,0.18);
  }

  /* Services side */
  .card--services {
    left: 70px; top: 60px;
    background: radial-gradient(ellipse at 75% 40%, #1f1a17 0%, var(--ink-dark) 65%);
    color: var(--text-light);
  }
  .wheel-art {
    position: absolute;
    left: 330px; top: 40px;
    width: 230px; height: 230px;
    border-radius: 50%;
    background: radial-gradient(circle, #3a3a3a 0%, #2a2420 40%, #5a2a10 62%, rgba(120,50,10,0.35) 75%, rgba(13,12,12,0) 100%);
    opacity: 0.85;
  }
  .services__heading {
    position: absolute; left: 44px; top: 62px;
    font-size: 24px; font-weight: 600; letter-spacing: 0.5px;
    color: var(--accent);
  }
  .services__rule {
    position: absolute; left: 44px; top: 100px;
    width: 170px; height: 1px; background: #d9d9d9;
  }
  .services__list {
    position: absolute; left: 44px; top: 114px;
    list-style: none;
    font-size: 15.5px; line-height: 24.5px; font-weight: 400;
  }
  .services__list li { position: relative; padding-left: 26px; }
  .services__list li::before {
    content: ""; position: absolute; left: 0; top: 7px;
    width: 11px; height: 11px; border-radius: 50%;
    background: var(--accent);
  }
  .brand--dark {
    position: absolute; right: 40px; top: 250px;
    display: flex; align-items: center; gap: 10px;
  }
  .brand__dot {
    width: 14px; height: 14px; border-radius: 50%;
    background: var(--accent);
  }
  .brand__name {
    font-size: 19px; font-weight: 600; color: var(--text-light);
  }

  /* Contact side */
  .card--contact {
    left: 490px; top: 474px;
    background: var(--card-white);
    color: var(--text-grey);
  }
  .brand--light {
    position: absolute; left: 320px; top: 58px;
  }
  .brand--light .brand__name {
    font-size: 30px; font-weight: 700; color: var(--text-grey);
  }
  .brand__rule {
    position: absolute; left: 320px; top: 104px;
    width: 280px; height: 1px; background: var(--line-soft);
  }
  .contact__rule-long {
    position: absolute; left: 40px; top: 190px;
    width: 560px; height: 1px; background: var(--accent);
  }
  .contact__name {
    position: absolute; left: 40px; top: 210px;
    font-size: 30px; font-weight: 700; color: var(--text-grey);
  }
  .contact__role {
    position: absolute; left: 40px; top: 252px;
    font-size: 18px; font-weight: 400; color: var(--accent);
  }
  .contact__rule-short {
    position: absolute; left: 40px; top: 284px;
    width: 260px; height: 1px; background: var(--accent);
  }
  .contact__details {
    position: absolute; left: 40px; top: 296px;
    list-style: none; font-size: 16px; line-height: 28px;
    color: var(--text-grey);
  }
  .contact__details li { display: flex; align-items: center; gap: 12px; }
  .contact__details svg { width: 15px; height: 15px; flex: none; }
</style>
</head>
<body>

<section class="card card--services" aria-label="Services side">
  <div class="wheel-art" role="img" aria-label="Alloy car wheel wrapped in flames"></div>
  <h2 class="services__heading">OUR SERVICES</h2>
  <div class="services__rule"></div>
  <ul class="services__list">
    <li>All Cars, 4WDs, Light trucks, makes and models</li>
    <li>Log book servicing</li>
    <li>General vehicle servicing</li>
    <li>Major vehicle servicing</li>
    <li>brake and clutch servicing and repairs</li>
    <li>Suspension repairs</li>
    <li>cooling systems</li>
    <li>All major and minor mechanical repairs</li>
    <li>minor electrical rewiring and repairs</li>
  </ul>
  <div class="brand brand--dark">
    <span class="brand__dot"></span>
    <span class="brand__name">Copper Heron Motor</span>
  </div>
</section>

<section class="card card--contact" aria-label="Contact side">
  <div class="brand brand--light">
    <span class="brand__name">Copper Heron Motor</span>
  </div>
  <div class="brand__rule"></div>
  <div class="contact__rule-long"></div>
  <h1 class="contact__name">Maree Tolland</h1>
  <p class="contact__role">Owner/ Mechanic</p>
  <div class="contact__rule-short"></div>
  <ul class="contact__details">
    <li>
      <svg viewBox="0 0 24 24" aria-hidden="true"><path fill="#f7931e" d="M6.6 10.8a15.1 15.1 0 0 0 6.6 6.6l2.2-2.2c.3-.3.7-.4 1-.2 1.1.4 2.3.6 3.6.6.6 0 1 .4 1 1V20c0 .6-.4 1-1 1A17 17 0 0 1 3 4c0-.6.4-1 1-1h3.5c.6 0 1 .4 1 1 0 1.3.2 2.5.6 3.6.1.3 0 .7-.2 1z"/></svg>
      <span>0413527806</span>
    </li>
    <li>
      <svg viewBox="0 0 24 24" aria-hidden="true"><rect x="3" y="5" width="18" height="14" rx="1.5" fill="none" stroke="#f7931e" stroke-width="2"/><path d="M3.5 6l8.5 7 8.5-7" fill="none" stroke="#f7931e" stroke-width="2"/></svg>
      <span>maree@copperheronmotor.com.au</span>
    </li>
  </ul>
</section>

</body>
</html>
```